Piedra Valley College-Larkspur Kickoff Days

I am the Student Activities Coordinator at Piedra Valley College-Larkspur. For Kickoff Days 2013, I need a standard poster 24x36 with the list of events happening. Our theme is based on the popular Thursday Late Laughs video "We Ride the Rails"
http://www.vidplexa-example.com/watch?v=K3pqTzWmBoA
Our theme is:
We're at the 'Spur!
Kickoff Days 2013
Graphics on the poster should reflect popular images/designs of TLL We Ride the Rails. However, the boat should be a steamboat instead of the yacht image.
Unfortunately, I have a lot of text to fit on the poster. Traditionally we go with 3 margins listing events. I'm attaching the word document of events and our logo to this proposal. I'll also attach a few google images of "We Ride the Rails" that align with the type of theme I'm looking for.
One last thing, our logo contains mountains listing all of the different campuses. Remove the campus names and mountains all together. Use simply the Colorado flag C and "Piedra Valley College".
Thanks for considering this brief!
Glen
Our college students love to ski and snowboard. In fact, one of our degrees is "Alpine Recreation Management". Their ages are 18-22.
Events

```html
<!DOCTYPE html>
<html lang="en">
<head>
<meta charset="utf-8">
<title>We're at the 'Spur! – Kickoff Days 2013</title>
<link rel="stylesheet" href="https://fonts.googleapis.com/css2?family=Archivo+Black&family=Arimo:wght@400;700&display=swap">
<style>
  :root {
    --page: #ffffff;
    --frame: #9a9a9a;
    --sky-red: #d9443a;
    --sky-orange: #ef8a3a;
    --sky-yellow: #fbd44a;
    --sky-pale: #fff6d6;
    --hill: #3fae6a;
    --water-light: #4a90cf;
    --water: #3d87c9;
    --deep-blue: #1b6ab2;
    --boat-light: #ffffff;
    --boat-grey: #c9c9c9;
    --navy: #26386b;
    --ink: #ffffff;
    --outline: #2a2a2a;
    --shadow-yellow: #ffe600;
    --text-dark: #222222;
  }
  * { box-sizing: border-box; margin: 0; padding: 0; }
  html, body { width: 900px; height: 1200px; overflow: hidden; background: var(--page); }
  body { position: relative; font-family: "Arimo", Arial, sans-serif; }

  .size-label {
    position: absolute; left: 104px; top: 50px;
    font-size: 12px; color: var(--text-dark);
  }
  .poster {
    position: absolute; left: 104px; top: 66px;
    width: 694px; height: 1085px;
    border: 1px solid var(--frame);
    overflow: hidden;
    background: linear-gradient(180deg,
      var(--sky-red) 0px, var(--sky-red) 150px,
      var(--sky-orange) 250px, var(--sky-yellow) 330px,
      var(--sky-pale) 390px, #ffffff 420px);
  }
  .brand {
    position: absolute; left: 510px; top: 28px;
    width: 154px; height: 80px;
    background: var(--navy);
    display: flex; align-items: center; justify-content: center;
    text-align: center;
    font-family: "Arimo", Arial, sans-serif; font-weight: 700;
    font-size: 17px; line-height: 19px; color: var(--ink);
    letter-spacing: -0.3px;
  }
  .headline {
    position: absolute; left: 0; top: 160px; width: 694px;
    text-align: center;
    font-family: "Archivo Black", "Arial Black", sans-serif;
    font-weight: 400;
    color: var(--ink);
    -webkit-text-stroke: 3px var(--outline);
    paint-order: stroke fill;
    transform: rotate(-2deg);
  }
  .headline-lead {
    display: block; font-size: 44px; line-height: 50px;
    text-shadow: 5px 5px 0 var(--shadow-yellow);
    margin-left: -30px;
  }
  .headline-main {
    display: block; font-size: 104px; line-height: 106px;
    letter-spacing: -2px;
    text-shadow: 7px 7px 0 var(--shadow-yellow);
    -webkit-text-stroke: 4px var(--outline);
  }
  .headline-sub {
    display: block; font-size: 32px; line-height: 36px;
    text-shadow: 4px 4px 0 var(--shadow-yellow);
    margin-left: 20px;
  }
  .scene {
    position: absolute; left: 0; top: 400px; width: 694px; height: 346px;
    display: block;
  }
  .schedule {
    position: absolute; left: 0; top: 746px; width: 694px; height: 339px;
    background: var(--deep-blue);
    color: var(--ink);
    font-size: 7px; line-height: 8.2px;
  }
  .schedule-col { position: absolute; top: 21px; width: 132px; }
  .schedule-col:nth-child(1) { left: 81px; }
  .schedule-col:nth-child(2) { left: 223px; }
  .schedule-col:nth-child(3) { left: 364px; }
  .schedule-col:nth-child(4) { left: 505px; }
  .event { margin-bottom: 8.2px; }
  .event-title { font-weight: 700; display: block; }
</style>
</head>
<body>
  <div class="size-label">Size 23x36</div>

  <main class="poster">
    <div class="brand">PIEDRA VALLEY<br>COLLEGE</div>

    <h1 class="headline">
      <span class="headline-lead">We're at the</span>
      <span class="headline-main">'SPUR!</span>
      <span class="headline-sub">Kickoff Days 2013</span>
    </h1>

    <svg class="scene" viewBox="0 0 694 346" width="694" height="346" role="img"
         aria-label="Illustration of a white paddle-wheel steamboat with twin black smokestacks, masts and yellow pennants on a blue lake, green hills behind">
      <defs>
        <linearGradient id="lake" x1="0" y1="0" x2="0" y2="1">
          <stop offset="0" stop-color="var(--water-light)"/>
          <stop offset="1" stop-color="var(--deep-blue)"/>
        </linearGradient>
        <linearGradient id="boat-area" x1="0" y1="0" x2="0" y2="1">
          <stop offset="0" stop-color="var(--boat-grey)" stop-opacity="0.35"/>
          <stop offset="0.55" stop-color="var(--boat-light)" stop-opacity="0.9"/>
          <stop offset="1" stop-color="var(--boat-grey)" stop-opacity="0.6"/>
        </linearGradient>
      </defs>
      <rect class="scene-sky" x="0" y="0" width="694" height="150" fill="#ffffff"/>
      <path class="scene-hills" d="M0 150 L0 118 C 90 96, 160 84, 240 92 C 330 100, 400 70, 480 76 C 560 82, 620 100, 694 106 L694 150 Z" fill="var(--hill)"/>
      <rect class="scene-lake" x="0" y="142" width="694" height="204" fill="url(#lake)"/>
      <rect class="scene-boat-area" x="44" y="6" width="562" height="250" rx="40" fill="url(#boat-area)"/>
    </svg>

    <section class="schedule" aria-label="Event schedule">
      <div class="schedule-col">
        <p class="event"><span class="event-title">Thursday August 22:</span>Residence Hall Move-In<br>12:00pm-3:00pm<br>Ridge Hall</p>
        <p class="event"><span class="event-title">Brunch</span>10:00am-1:00pm<br>Dining Hall</p>
        <p class="event"><span class="event-title">International Students Orientation</span>3:00pm<br>Birch 121</p>
        <p class="event"><span class="event-title">Dinner</span>5:00pm-6:30pm<br>Dining Hall</p>
        <p class="event">Hot Springs Waterslide Party<br>7:00pm-9:00pm<br>Old Mill Hot Springs</p>
        <p class="event"><span class="event-title">Friday August 23:</span>Breakfast<br>7:30am-9:00am<br>Dining Hall</p>
        <p class="event"><span class="event-title">Hike Silver Creek Falls</span>9:00am-11:30am<br>Shuttle leaves Ridge Hall at 8:30am</p>
        <p class="event"><span class="event-title">BBQ and Faculty Ice Cream Social</span>12:00pm-1:30pm<br>Dining Hall</p>
      </div>
      <div class="schedule-col">
        <p class="event"><span class="event-title">Kick Off Party: Inflatables</span>1:30pm-4:00pm<br>Upper Parking Lot</p>
        <p class="event"><span class="event-title">Dinner</span>5:00pm-6:00pm<br>Dining Hall</p>
        <p class="event"><span class="event-title">Free Concert</span>7:00pm<br>Larkspur Resort Base<br>(LRT Buses to Resort,<br>5:35pm Last Bus)</p>
        <p class="event"><span class="event-title">Saturday August 24:</span>Main Street Farmers Market<br>9:00am-2:00pm<br>8th &amp; Elm (walking dist.)</p>
        <p class="event"><span class="event-title">Brunch</span>10:00am-1:00pm<br>Dining Hall</p>
        <p class="event"><span class="event-title">Juniper Park Hot Springs</span>2:00pm-5:00pm<br>Shuttle leaves Ridge Hall at 1:30pm</p>
        <p class="event"><span class="event-title">Dinner</span>5:00-6:00pm<br>Dining Hall</p>
        <p class="event"><span class="event-title">Free Movie on the Mountain:<br>Starfall Trials</span></p>
      </div>
      <div class="schedule-col">
        <p class="event">8:00pm<br>(LRT Buses to Resort, 5:35pm Last<br>Bus)</p>
        <p class="event"><span class="event-title">Sunday August 25:</span>Brunch<br>10:00am-1:00pm<br>Dining Hall</p>
        <p class="event"><span class="event-title">Alpine Slide/Volleyball</span>2:00pm-4:00pm<br>Meet at Tamarack Hill</p>
        <p class="event"><span class="event-title">Dinner</span>5:00pm-6:00pm<br>Dining Hall</p>
        <p class="event"><span class="event-title">Mandatory All Hall Meeting</span>6:00pm<br>Auditorium</p>
        <p class="event"><span class="event-title">RHA Super Sunday Program</span>8:00pm<br>Ridge Hall: MPR</p>
        <p class="event"><span class="event-title">Monday August 26:</span>Regular Dining Hall Hours Begin</p>
        <p class="event"><span class="event-title">"Being Alone Sucks!"</span>9:00pm<br>Auditorium<br><span class="event-title">Tuesday August 27:</span>Newly Roommate Game</p>
      </div>
      <div class="schedule-col">
        <p class="event">7:00pm-8:00pm<br>Ridge Hall: MPR</p>
        <p class="event"><span class="event-title">Free Gelato</span>8:00pm-9:00pm<br>Dolce Cone 7th and Pine</p>
        <p class="event"><span class="event-title">Wednesday August 28:</span>Free Bowling<br>9:00pm<br>Powder Lanes</p>
        <p class="event"><span class="event-title">Thursday August 29:</span>Club Fair<br>10:00am-2:00pm<br>Dining Hall</p>
        <p class="event"><span class="event-title">Black Light Dodgeball</span>9:00pm<br>Gym</p>
        <p class="event"><span class="event-title">Friday August 30:</span>Late Night Climbing<br>9:00pm<br>Gym</p>
        <p class="event">ALL EVENTS ARE FREE<br>UNLESS OTHERWISE NOTED</p>
      </div>
    </section>
  </main>
</body>
</html>
```